Flyer Needed for Westland Advocacy Summit 2017

We need a flyer designed for a save the date for Verdant Goods Forum in California on August 23, 2017. The lobby day is taking place in Sacramento so please design the flyer using these details.

Requirements
Must have
• - Date must be clear
Nice to have
• - Must have "save the date"
• - Something that catches your eye

```html
<!DOCTYPE html>
<html lang="en">
<head>
<meta charset="utf-8">
<title>Verdant Goods Forum – Save the Date</title>
<link href="https://fonts.googleapis.com/css2?family=Roboto+Condensed:ital,wght@0,300;0,400;0,700;1,300&display=swap" rel="stylesheet">
<style>
  :root {
    --page-bg: #121212;
    --card-top: #4f6340;
    --card-mid: #43563a;
    --card-deep: #0f170b;
    --title-green-light: #93cc45;
    --title-green-dark: #5d9628;
    --band-green: #7ba83b;
    --band-text: #1a2410;
    --glow-bright: rgba(176, 235, 96, 0.85);
    --glow-soft: rgba(143, 209, 74, 0.45);
    --skyline-dark: rgba(24, 36, 18, 0.9);
    --water-dark: rgba(16, 26, 12, 0.85);
    --white: #ffffff;
  }
  * { margin: 0; padding: 0; box-sizing: border-box; }
  html, body {
    width: 1200px; height: 1200px; overflow: hidden;
    background: var(--page-bg);
    font-family: "Roboto Condensed", sans-serif;
  }
  .flyer {
    position: absolute; left: 30px; top: 201px;
    width: 1140px; height: 798px; overflow: hidden;
    background: linear-gradient(180deg, var(--card-top) 0%, var(--card-mid) 50%, var(--card-deep) 100%);
  }
  .city-photo {
    position: absolute; left: 0; top: 210px; width: 100%; height: 588px;
    background:
      /* bright lit roadway sweeping to the lower left */
      radial-gradient(ellipse 30% 38% at 26% 88%, var(--glow-bright), transparent 70%),
      radial-gradient(ellipse 48% 30% at 30% 72%, var(--glow-soft), transparent 72%),
      /* bridge tower glow on the left */
      radial-gradient(ellipse 12% 45% at 18% 40%, rgba(143, 209, 74, 0.3), transparent 75%),
      /* city lights along the horizon */
      radial-gradient(ellipse 42% 14% at 72% 60%, rgba(176, 235, 96, 0.45), transparent 75%),
      radial-gradient(ellipse 55% 9% at 60% 66%, rgba(200, 245, 130, 0.35), transparent 80%),
      /* skyline mass, water and dark foreground */
      linear-gradient(180deg,
        rgba(59, 76, 48, 0) 0%,
        rgba(59, 76, 48, 0) 38%,
        var(--skyline-dark) 48%,
        rgba(40, 58, 30, 0.75) 64%,
        var(--water-dark) 72%,
        rgba(30, 46, 22, 0.8) 82%,
        var(--card-deep) 100%);
  }
  .line {
    position: absolute; white-space: nowrap; line-height: 1; text-align: center;
  }
  .title {
    left: 0; width: 100%; top: 41px;
    font-size: 99px; font-weight: 700; letter-spacing: -1px;
    background: linear-gradient(180deg, var(--title-green-light), var(--title-green-dark));
    -webkit-background-clip: text; background-clip: text; color: transparent;
    filter: drop-shadow(3px 5px 4px rgba(0,0,0,0.45));
  }
  .details { left: 108px; right: 0; color: var(--white); }
  .location { top: 159px; font-size: 93px; font-weight: 300; }
  .save-date {
    top: 274px; font-size: 112px; font-weight: 300;
    text-shadow: 4px 5px 3px rgba(0,0,0,0.55);
  }
  .save-date .small { font-size: 72px; }
  .event-date { top: 390px; font-size: 73px; font-weight: 300; font-style: italic; }
  .more-info {
    top: 623px; right: 64px; left: auto;
    font-size: 44px; font-weight: 400; color: var(--white);
  }
  .contact-band {
    position: absolute; left: 0; top: 682px; width: 100%; height: 68px;
    background: var(--band-green);
  }
  .contact-text {
    left: 70px; top: 691px; text-align: left;
    font-size: 46px; font-weight: 300; color: var(--band-text); letter-spacing: -0.5px;
    word-spacing: 1px;
  }
  .contact-text .divider { margin: 0 22px; }
</style>
</head>
<body>
  <main class="flyer">
    <div class="city-photo" role="img" aria-label="Night photo of a lit suspension bridge and city skyline over the water, tinted green"></div>

    <h1 class="line title">VERDANT GOODS FORUM</h1>
    <p class="line details location">IN CALIFORNIA</p>
    <p class="line details save-date">SAVE <span class="small">THE</span> DATE</p>
    <p class="line details event-date">AUGUST 23, 2017.</p>

    <p class="line more-info">FOR MORE INFO</p>
    <div class="contact-band"></div>
    <p class="line contact-text">CONTACT US NOW 5550142<span class="divider">|</span>WWW.VERDANTGF.COM</p>
  </main>
</body>
</html>
```